we need a business card design for a professional painting business. This company has been up and going for about ten years. However it needs an new logo. we want this business card to be modern eye catching and easy to read. I currently have been looking for VC logos but can not find one that suits our needs. This Design should be Our start to a new beginning.
Industry/Entity Type
Painting
Contact Information for Business Card
Varetti Coatings Inc.
Licensed & Insured
Tomas Varetti
Phone(631)384-4562
Fax (555) 730-2418
E-mail varetticoatingsinc@mailbox.example
Requirements
Must have
- a new logo with  VC and i would like it to be in black and white.
i would also like the front to be a solid black with the logo only and then the back to have the information.

```html
<!DOCTYPE html>
<html lang="en">
<head>
<meta charset="utf-8">
<title>Varetti Coatings Inc. – Business Card</title>
<link rel="stylesheet" href="https://fonts.googleapis.com/css2?family=Arimo:wght@400;700&family=PT+Sans+Narrow:wght@700&display=swap">
<style>
  :root {
    --backdrop: #3a3838;
    --card-black: #050505;
    --card-white: #ffffff;
    --mark-dark: #231f20;
    --band: #231f20;
    --ink: #111111;
    --accent-red: #e8111c;
    --icon-grey: #c9cbcf;
  }
  * { margin: 0; padding: 0; box-sizing: border-box; }
  html, body {
    width: 1200px;
    height: 1200px;
    overflow: hidden;
    background: var(--backdrop);
  }
  .canvas {
    position: relative;
    width: 1200px;
    height: 1200px;
  }
  .card {
    position: absolute;
    left: 162px;
    width: 876px;
    height: 500px;
    overflow: hidden;
  }
  /* Front: solid black with identity only */
  .card-front {
    top: 70px;
    background: var(--card-black);
  }
  .front-mark {
    position: absolute;
    left: 373px;
    top: 120px;
    width: 130px;
    height: 130px;
    background: #2a2627;
  }
  .front-name {
    position: absolute;
    left: 0;
    right: 0;
    top: 282px;
    text-align: center;
    color: var(--card-white);
    font-family: "PT Sans Narrow", sans-serif;
    font-weight: 700;
    font-size: 34px;
    letter-spacing: 0.5px;
    text-transform: uppercase;
  }
  /* Back: contact information */
  .card-back {
    top: 630px;
    background: var(--card-white);
  }
  .back-mark {
    position: absolute;
    left: 48px;
    top: 42px;
    width: 128px;
    height: 128px;
    background: var(--mark-dark);
  }
  .company-name {
    position: absolute;
    left: 200px;
    top: 62px;
    color: var(--ink);
    font-family: "PT Sans Narrow", sans-serif;
    font-weight: 700;
    font-size: 36px;
    text-transform: uppercase;
    letter-spacing: -0.3px;
  }
  .tagline {
    position: absolute;
    left: 200px;
    top: 110px;
    color: var(--accent-red);
    font-family: "Arimo", sans-serif;
    font-size: 24px;
    line-height: 28px;
    text-transform: uppercase;
  }
  .name-band {
    position: absolute;
    left: 0;
    right: 0;
    top: 210px;
    height: 46px;
    background: var(--band);
  }
  .person-name {
    position: absolute;
    left: 380px;
    top: 8px;
    color: var(--card-white);
    font-family: "Arimo", sans-serif;
    font-weight: 700;
    font-size: 27px;
    letter-spacing: 0.5px;
  }
  .person-role {
    position: absolute;
    left: 410px;
    top: 262px;
    color: var(--ink);
    font-family: "Arimo", sans-serif;
    font-size: 23px;
  }
  .contact {
    position: absolute;
    left: 520px;
    top: 360px;
    color: var(--ink);
    font-family: "Arimo", sans-serif;
    font-size: 22px;
    line-height: 28px;
  }
  .contact-line { display: flex; align-items: center; white-space: nowrap; }
  .contact-line svg { margin-right: 8px; }
  .contact-indent { padding-left: 0; }
  .contact-email { font-size: 19px; }
</style>
</head>
<body>
<main class="canvas">
  <section class="card card-front" aria-label="Card front">
    <div class="front-mark"></div>
    <p class="front-name">Varetti Coatings Inc.</p>
  </section>

  <section class="card card-back" aria-label="Card back">
    <div class="back-mark"></div>
    <h1 class="company-name">Varetti Coatings Inc.</h1>
    <p class="tagline">Licensed &amp; Insured<br>Professional Painter</p>

    <div class="name-band">
      <p class="person-name">Tomas Varetti</p>
    </div>
    <p class="person-role">Owner/Manager</p>

    <div class="contact">
      <p class="contact-line">
        <svg width="28" height="28" viewBox="0 0 28 28" aria-hidden="true">
          <circle cx="14" cy="14" r="13" fill="var(--icon-grey)" stroke="#8b8e93" stroke-width="1"/>
          <rect x="10" y="7" width="8" height="14" rx="1.5" fill="#222"/>
          <rect x="11.5" y="9" width="5" height="4" fill="#ddd"/>
        </svg>
        555.217.8093
      </p>
      <p class="contact-line contact-indent">Fax 555.730.2418</p>
      <p class="contact-line contact-email">varetticoatingsinc@mailbox.example</p>
    </div>
  </section>
</main>
</body>
</html>
```